Corvell Executive Search - New Business Card Design Project

We are an executive search firm called Corvell Executive Search based in the UK. We require a custom design for a business card. We're looking to convey a professional service to executives for executive search recruitment services. In terms of colours, we like dark blues and grays (maybe even silver incorporated somewhere if we go for a foiled type of card) but we're open to your artistic flare. See our current logo in attachments. We are totally open on design so long as the design is slick and professional.
Updates

Thanks for all your contributions of various designs. I have to say the quality of work has been amazing which is going to make our job quite difficult in the coming days on making a decision. Thanks to you all that have taken the time to submit designs thus far. We'll keep on reviewing and try to narrow down our selection as soon as possible.

Target Market(s)

Executive Search

Industry/Entity Type

Recruitment

Contact Information for Business Card

Corvell Executive Search,
Exclusively Sourcing & Hiring Senior Leaders
Dominic Haverley, Managing Director,
07742 318906
0117 468 2917
dominic@corvellexecutive.example
corvellexecutive.example
47 Linden Court, Marsh Lane, Bristol, BS9 7QT

Font styles to use
Sans Serif
Other font styles liked:
• Roboto (which is used in our logo)

Requirements
Must have
• Our logo (It has a subtle fade on it from #02071d at top to #333649 at bottom)
• The logo can be on one side or both sides
• Must be elegant and professional
• We have 2nd slogan CONSULT | INSPIRE | INNOVATE | DELIVER which can be incorporated into the card
Nice to have
• Use of blues and grey colours
• Compatible with similar styling to our website corvellexecutive.example
Should not have
• Must not be overly brash
• Must not contain cartoon characters

```html
<!DOCTYPE html>
<html lang="en">
<head>
<meta charset="utf-8">
<title>Corvell Executive Search – Business Card</title>
<link rel="stylesheet" href="https://fonts.googleapis.com/css2?family=Roboto:wght@400;500;700&family=Lora:wght@400&display=swap">
<style>
  :root {
    --stage: #111426;
    --card-dark: #0f1225;
    --card-light: #ffffff;
    --shadow: #070912;
    --brand-square: #1c2035;
    --ink: #1a1c2a;
    --muted: #9a9ba6;
    --on-dark: #ffffff;
  }
  * { margin: 0; padding: 0; box-sizing: border-box; }
  html, body { width: 1200px; height: 1200px; overflow: hidden; background: var(--stage); }
  .stage { position: relative; width: 1200px; height: 1200px; font-family: "Roboto", Arial, sans-serif; }
  .card-shadow { position: absolute; background: var(--shadow); }
  .card { position: absolute; overflow: hidden; background: var(--card-dark); }
  .card svg.shapes { position: absolute; inset: 0; }
  .abs { position: absolute; white-space: nowrap; }

  .front { left: 54px; top: 75px; width: 772px; height: 485px; }
  .back { left: 335px; top: 657px; width: 771px; height: 483px; }

  .brand { position: absolute; display: flex; align-items: center; color: var(--ink); font-weight: 500; white-space: nowrap; }
  .brand-square { display: block; background: var(--brand-square); flex: none; }
  .front .brand { left: 323px; top: 248px; gap: 12px; font-size: 22px; }
  .front .brand-square { width: 36px; height: 36px; }
  .back .brand { left: 39px; top: 80px; gap: 10px; font-size: 17px; }
  .back .brand-square { width: 28px; height: 28px; }

  .slogan {
    font-family: "Lora", Georgia, serif;
    font-size: 12px; letter-spacing: 0.08em; color: var(--on-dark);
    transform-origin: left bottom; transform: rotate(-31.5deg);
  }
  .front .strapline { left: 325px; top: 395px; font-size: 12px; line-height: 19px; color: var(--ink); }

  .back .strapline {
    font-size: 11px; line-height: 15px; color: var(--ink);
    transform-origin: left bottom; transform: rotate(-30.5deg);
  }

  .person-name { left: 516px; top: 41px; font-size: 21px; font-weight: 500; color: var(--on-dark); }
  .person-name .surname { color: var(--muted); }
  .person-role { left: 517px; top: 73px; font-size: 12px; color: #d8d9e0; }

  .contact { left: 228px; font-size: 12px; color: #e6e7ec; display: flex; align-items: center; gap: 24px; }
  .contact .badge {
    width: 20px; height: 20px; border-radius: 50%; background: var(--muted);
    color: #e9e9ef; font-size: 10px; display: flex; align-items: center; justify-content: center;
  }
  .address { left: 583px; top: 430px; font-size: 12px; line-height: 18px; color: var(--ink); }
</style>
</head>
<body>
<div class="stage">
  <div class="card-shadow" style="left:30px;top:118px;width:772px;height:484px;"></div>
  <section class="card front">
    <svg class="shapes" width="772" height="485" viewBox="0 0 772 485">
      <polygon points="576,0 772,0 772,315 468,485 0,485 0,347" fill="#ffffff"/>
    </svg>
    <p class="abs slogan" style="left:164px;top:213px;">CONSULT | INSPIRE | INNOVATE | DELIVER</p>
    <div class="brand">
      <span class="brand-square"></span>
      <span class="brand-name">Corvell Executive Search</span>
    </div>
    <p class="abs strapline">Corvell Executive Search,<br>Exclusively Sourcing &amp; Hiring Senior Leaders</p>
  </section>

  <div class="card-shadow" style="left:323px;top:679px;width:770px;height:483px;"></div>
  <section class="card back">
    <svg class="shapes" width="771" height="483" viewBox="0 0 771 483">
      <polygon points="0,0 574,0 0,347" fill="#ffffff"/>
      <polygon points="771,316 771,483 467,483" fill="#ffffff"/>
    </svg>
    <div class="brand">
      <span class="brand-square"></span>
      <span class="brand-name">Corvell Executive Search</span>
    </div>
    <p class="abs strapline" style="left:70px;top:252px;">Corvell Executive Search<br>Exclusively Sourcing &amp; Hiring Senior Leaders</p>
    <p class="abs person-name">Dominic <span class="surname">Haverley</span></p>
    <p class="abs person-role">Managing Director</p>
    <p class="abs contact" style="top:257px;"><span class="badge">T</span>07742 318906, 0117 468 2917</p>
    <p class="abs contact" style="top:301px;"><span class="badge">E</span>dominic@corvellexecutive.example</p>
    <p class="abs contact" style="top:345px;"><span class="badge">W</span>www.corvellexecutive.example</p>
    <p class="abs address">47 Linden Court, Marsh Lane,<br>Bristol, BS9 7QT</p>
  </section>
</div>
</body>
</html>
```